Our Server Lantern requires an Email Marketing Design template

Our Server Lantern are a rapidly expanding UK based internet hosting company that have just re-branded through Pixel Meadow.
We provide internet based services such as website hosting, dedicated and managed servers, domain names as well as email solutions to name a few. We pride ourselves on being able to provide a comprehensive, secure, future proofed and scalable platform for our clients to communicate and do business on.
Our Server Lantern are looking to go live with a new website on 1st August. In preparation for this we would like to have an HTML Email Template designed for our launch!
We are also having a really big push on the reseller market allowing potential resellers and their end users to manage their own services via a consolidated portal with many features and functions that will grow over time.

Target Market(s)
We have 3 core target markets, the end user who would be the likes of web designers or developers. A reseller market who would want to resell our hosted services and the final target market would be a business client that would want high end server and hosting solutions.
Industry/Entity Type
Internet Service Provider
Requirements
Must have
- To ensure it is inline with the new brand (see attached files).

```html
<!DOCTYPE html>
<html lang="en">
<head>
<meta charset="utf-8">
<title>Our Server Lantern – Launch Email</title>
<link href="https://fonts.googleapis.com/css2?family=Oswald:wght@400;500;700&family=Open+Sans:wght@400;600;700&display=swap" rel="stylesheet">
<style>
:root{
  --teal:#1bb5be;
  --teal-dark:#128e97;
  --teal-deep:#0d747c;
  --teal-light:#86d6dc;
  --teal-pale:#c9eef0;
  --navy:#1b2430;
  --ink:#2a2f36;
  --grey:#ececec;
  --grey-mid:#d9d9d9;
  --white:#ffffff;
  --text:#444b52;
}
*{box-sizing:border-box;margin:0;padding:0}
html,body{width:1200px;height:5180px;overflow:hidden;background:var(--white)}
body{position:relative;font-family:"Open Sans",Arial,sans-serif;color:var(--text)}
.abs{position:absolute}
.head{font-family:"Oswald","Arial Narrow",sans-serif;text-transform:uppercase}
.photo{position:absolute}

/* hero */
.hero{left:0;top:0;width:1200px;height:842px;overflow:hidden}
.hero .photo{inset:0;background:linear-gradient(120deg,#e9ecef 0%,#c9b8a6 35%,#8a7564 55%,#4f6f8f 80%,#2f4e6e 100%)}
.brand{left:28px;top:28px;display:flex;align-items:center;gap:16px}
.brand-dot{width:72px;height:72px;border-radius:50%;background:var(--teal)}
.brand-name{font-family:"Oswald","Arial Narrow",sans-serif;font-size:40px;line-height:40px;font-weight:500;color:var(--ink);width:240px}
.top-links{right:30px;top:24px;font-family:"Oswald",sans-serif;font-size:22px;color:var(--white);letter-spacing:1px}
.socials{right:30px;top:62px;display:flex;gap:10px}
.socials span{width:46px;height:46px;border-radius:50%;border:3px solid var(--white)}
.hero-title{left:30px;top:282px;color:var(--white)}
.hero-title .small{font-size:52px;line-height:56px;font-weight:500;display:block}
.hero-title .big{font-size:74px;line-height:82px;font-weight:700;display:block}
.btn{display:flex;align-items:center;justify-content:center;font-family:"Oswald",sans-serif;text-transform:uppercase;color:var(--white);background:var(--teal)}
.hero-btn{left:30px;top:704px;width:226px;height:96px;font-size:32px}

/* section titles */
.section-title{left:0;width:1200px;text-align:center;font-family:"Oswald",sans-serif;font-size:44px;font-weight:500;color:var(--ink);text-transform:uppercase}
.section-title.left{text-align:left;left:22px}

/* plans */
.plan{top:971px;width:224px;height:454px;background:var(--grey)}
.plan-icon{left:58px;top:0;width:108px;height:108px;border-radius:50%;background:var(--teal);border:8px solid var(--white)}
.plan-name{left:0;top:170px;width:100%;text-align:center;font-family:"Oswald",sans-serif;font-size:34px;color:var(--ink)}
.plan-price{left:0;top:224px;width:100%;text-align:center;font-family:"Oswald",sans-serif;color:var(--ink)}
.plan-price .from{font-family:"Open Sans",sans-serif;font-size:20px}
.plan-price .amt{font-size:64px;font-weight:500}
.plan-price .mo{font-size:22px;vertical-align:28px}
.plan-foot{left:0;bottom:0;width:100%;height:112px;background:var(--teal)}
.plan-order{left:32px;top:28px;width:160px;height:56px;background:var(--white);color:var(--ink);font-family:"Oswald",sans-serif;font-size:24px;display:flex;align-items:center;justify-content:center}

/* services */
.service{left:0;width:1200px;height:304px;overflow:hidden;background:var(--navy)}
.service .photo{left:560px;top:0;width:640px;height:100%;clip-path:polygon(120px 0,100% 0,100% 100%,0 100%)}
.service-name{left:44px;top:26px;font-size:46px;font-weight:500;color:var(--white)}
.service-price{left:0;top:104px;width:300px;height:108px;background:var(--teal-dark);padding:10px 0 0 44px;color:var(--white)}
.service-price .from{font-size:24px;display:block}
.service-price .amt{font-family:"Oswald",sans-serif;font-size:48px;line-height:54px;color:var(--teal-light)}
.service-btn{left:44px;top:228px;width:166px;height:52px;font-size:24px}

/* why */
.why-tile{top:2577px;width:240px;height:337px;color:var(--white)}
.why-tile svg{position:absolute;left:26px;top:34px}
.why-label{position:absolute;left:22px;bottom:26px;font-family:"Oswald",sans-serif;font-size:34px;line-height:36px;font-weight:500;text-transform:uppercase}

/* newsletter */
.newsletter{left:43px;top:2979px;width:1114px;height:172px;background:var(--teal);border:6px solid var(--white);outline:4px solid var(--teal)}
.newsletter-text{left:290px;top:16px;font-family:"Oswald",sans-serif;font-size:58px;line-height:60px;font-weight:500;color:var(--white);text-transform:uppercase}

/* earn */
.earn{left:0;top:3216px;width:1200px;height:259px;background:var(--grey)}
.earn-right{left:600px;top:0;width:600px;height:259px;background:var(--teal-light);clip-path:polygon(60px 0,100% 0,100% 100%,0 100%)}
.earn-title{font-family:"Oswald",sans-serif;font-size:42px;font-weight:500;color:var(--ink);text-transform:uppercase}
.earn-btn{width:430px;height:92px;font-size:32px}

/* blog */
.blog-card{background:var(--grey)}
.blog-meta{font-size:18px;color:var(--ink);margin-bottom:14px}
.blog-title{font-family:"Oswald",sans-serif;font-size:30px;color:var(--teal-dark);margin-bottom:12px}
.blog-body{font-size:20px;line-height:29px;color:var(--text)}
.blog-more{font-size:19px;color:var(--teal);margin-top:18px}

/* footer */
.footer{left:0;top:4748px;width:1200px;height:432px;background:var(--navy)}
.footer-right{left:520px;top:0;width:680px;height:432px;background:var(--teal);clip-path:polygon(110px 0,100% 0,100% 100%,0 100%)}
.footer h4{font-family:"Open Sans",sans-serif;font-size:22px;font-weight:700;color:var(--white);text-transform:uppercase}
.footer p{font-size:20px;line-height:30px;color:var(--white)}
.footer .teal{color:var(--teal)}
.footer-socials{display:flex;gap:10px}
.footer-socials span{width:44px;height:44px;border-radius:50%;border:3px solid #9aa3ad}
</style>
</head>
<body>

<!-- Hero -->
<header class="hero abs">
  <div class="photo" role="img" aria-label="Smiling couple on a sofa looking at a tablet together"></div>
  <div class="brand abs"><span class="brand-dot"></span><span class="brand-name">Our Server Lantern</span></div>
  <div class="top-links abs">REGISTER &nbsp;|&nbsp; SIGN IN</div>
  <div class="socials abs"><span></span><span></span><span></span><span></span></div>
  <h1 class="hero-title abs head"><span class="small">Empowering you</span><span class="small">to take control of your</span><span class="big">Internet Bubble</span></h1>
  <a class="btn hero-btn abs">Empower me</a>
</header>

<!-- Shared hosting -->
<h2 class="section-title left abs" style="top:880px">Shared Hosting</h2>

<div class="plan abs" style="left:26px">
  <div class="plan-icon abs"></div>
  <div class="plan-name abs">HOME</div>
  <div class="plan-price abs"><span class="from">From </span><span class="amt">£4</span><span class="mo">.99 /mo</span></div>
  <div class="plan-foot abs"><div class="plan-order abs">ORDER NOW</div></div>
</div>
<div class="plan abs" style="left:324px">
  <div class="plan-icon abs"></div>
  <div class="plan-name abs">BUSINESS</div>
  <div class="plan-price abs"><span class="from">From </span><span class="amt">£9</span><span class="mo">.99 /mo</span></div>
  <div class="plan-foot abs"><div class="plan-order abs">ORDER NOW</div></div>
</div>
<div class="plan abs" style="left:617px">
  <div class="plan-icon abs"></div>
  <div class="plan-name abs">PROFESSIONAL</div>
  <div class="plan-price abs"><span class="from">From </span><span class="amt">£19</span><span class="mo">.99 /mo</span></div>
  <div class="plan-foot abs"><div class="plan-order abs">ORDER NOW</div></div>
</div>
<div class="plan abs" style="left:915px">
  <div class="plan-icon abs"></div>
  <div class="plan-name abs">PREMIUM</div>
  <div class="plan-price abs"><span class="from">From </span><span class="amt">£34</span><span class="mo">.99 /mo</span></div>
  <div class="plan-foot abs"><div class="plan-order abs">ORDER NOW</div></div>
</div>

<!-- Services -->
<section class="service abs" style="top:1502px">
  <div class="photo" role="img" aria-label="Two technicians working at a server rack" style="background:linear-gradient(90deg,#3b4450,#7a8591 45%,#c9ccd0)"></div>
  <h3 class="service-name abs head">Dedicated Server</h3>
  <div class="service-price abs"><span class="from">From only</span><span class="amt">£39</span> <span class="from" style="display:inline">p/m</span></div>
  <a class="btn service-btn abs">ORDER NOW</a>
</section>
<section class="service abs" style="top:1810px">
  <div class="photo" role="img" aria-label="Smiling man in glasses working at a laptop" style="background:linear-gradient(90deg,#5a4a3c,#9b8470 45%,#d8cbbd)"></div>
  <h3 class="service-name abs head">Domain Name</h3>
  <div class="service-price abs"><span class="from">From only</span><span class="amt">£29</span> <span class="from" style="display:inline">p/m</span></div>
  <a class="btn service-btn abs">ORDER NOW</a>
</section>
<section class="service abs" style="top:2118px">
  <div class="photo" role="img" aria-label="Engineer in a suit standing beside server cabinets" style="background:linear-gradient(90deg,#2e3d4c,#6f8193 45%,#e4e7ea)"></div>
  <h3 class="service-name abs head">VPS</h3>
  <div class="service-price abs"><span class="from">From only</span><span class="amt">£19</span> <span class="from" style="display:inline">p/m</span></div>
  <a class="btn service-btn abs">ORDER NOW</a>
</section>

<!-- Why choose us -->
<h2 class="section-title abs" style="top:2474px">Why choose us?</h2>

<div class="why-tile abs" style="left:0;background:var(--teal-light)">
  <svg width="90" height="90" viewBox="0 0 90 90" fill="none" stroke="#fff" stroke-width="5"><path d="M78 45a33 33 0 1 1-10-24"/><path d="M70 8v16H54"/><text x="45" y="56" fill="#fff" stroke="none" font-family="Oswald" font-size="30" text-anchor="middle">24</text></svg>
  <div class="why-label">Free 24x7<br>Support</div>
</div>
<div class="why-tile abs" style="left:240px;background:var(--teal)">
  <svg width="90" height="90" viewBox="0 0 90 90" fill="none" stroke="#fff" stroke-width="5"><rect x="8" y="10" width="40" height="30"/><rect x="42" y="50" width="40" height="30"/><path d="M20 48v18h16M70 42V24H54"/></svg>
  <div class="why-label">Free<br>Migration</div>
</div>
<div class="why-tile abs" style="left:480px;background:var(--teal-dark)">
  <svg width="90" height="90" viewBox="0 0 90 90" fill="none" stroke="#fff" stroke-width="5"><circle cx="45" cy="45" r="36"/><line x1="20" y1="70" x2="70" y2="20"/><text x="45" y="56" fill="#fff" stroke="none" font-family="Oswald" font-size="32" text-anchor="middle">£</text></svg>
  <div class="why-label">No Hidden<br>Charges</div>
</div>
<div class="why-tile abs" style="left:720px;background:var(--teal-deep)">
  <svg width="90" height="90" viewBox="0 0 90 90" fill="#fff"><path d="M45 10 82 44H72v36H54V58H36v22H18V44H8z"/></svg>
  <div class="why-label">Gret Value<br>Domain Name</div>
</div>
<div class="why-tile abs" style="left:960px;background:#0c6a71">
  <svg width="90" height="90" viewBox="0 0 90 90" fill="#fff"><path d="M45 80 12 46C2 34 8 14 25 14c9 0 16 6 20 14 4-8 11-14 20-14 17 0 23 20 13 32z"/></svg>
  <div class="why-label">Our Customer<br>Love Us</div>
</div>

<!-- Newsletter -->
<div class="newsletter abs">
  <svg class="abs" style="left:150px;top:32px" width="118" height="96" viewBox="0 0 118 96" fill="none" stroke="#fff" stroke-width="5"><rect x="20" y="20" width="92" height="64"/><path d="M20 20l46 36 46-36"/><line x1="0" y1="40" x2="14" y2="40"/><line x1="4" y1="56" x2="14" y2="56"/></svg>
  <div class="newsletter-text abs">Sign-up to<br>our monthly newsletter</div>
</div>

<!-- Reseller / affiliate -->
<section class="earn abs">
  <div class="earn-right abs"></div>
  <svg class="abs" style="left:68px;top:34px" width="64" height="60" viewBox="0 0 64 60" fill="none" stroke="var(--teal)" stroke-width="5"><path d="M8 30l14-14 10 10 14-14 10 10"/><path d="M8 30v24h48V24"/></svg>
  <div class="earn-title abs" style="left:146px;top:36px">Become a Reseller</div>
  <a class="btn earn-btn abs" style="left:82px;top:130px">EARN MONEY NOW</a>
  <svg class="abs" style="left:690px;top:32px" width="64" height="64" viewBox="0 0 64 64" fill="none" stroke="var(--teal-deep)" stroke-width="5"><circle cx="32" cy="32" r="12"/><path d="M32 4v12M32 48v12M4 32h12M48 32h12M12 12l8 8M44 44l8 8M52 12l-8 8M12 52l8-8"/></svg>
  <div class="earn-title abs" style="left:770px;top:36px">Affiliate Program</div>
  <a class="btn earn-btn abs" style="left:690px;top:130px;background:var(--teal-dark)">JOIN NOW</a>
</section>

<!-- Blog -->
<h2 class="section-title abs" style="top:3556px">Latest Blog</h2>

<div class="photo" role="img" aria-label="Business colleagues gathered around a laptop" style="left:22px;top:3713px;width:376px;height:604px;background:linear-gradient(160deg,#4a5662,#a9b2ba 55%,#e1e4e6)"></div>
<article class="blog-card abs" style="left:22px;top:4317px;width:376px;height:388px;padding:26px 22px">
  <div class="blog-meta">Lorem, Dosis Ipsum</div>
  <div class="blog-title">Lorem Ipsum</div>
  <p class="blog-body">In publishing and graphic design, lorem ipsum is a filler text commonly used to demonstrate the graphic elements.</p>
  <div class="blog-more">Read more →</div>
</article>

<div class="photo" role="img" aria-label="Engineer standing in a data centre aisle" style="left:412px;top:3713px;width:376px;height:582px;background:linear-gradient(180deg,#2f3f52,#7d8ea0 60%,#cfd6dc)"></div>
<article class="blog-card abs" style="left:412px;top:4295px;width:376px;height:430px;padding:26px 22px">
  <div class="blog-meta">Lorem, Dosis Ipsum</div>
  <div class="blog-title">Lorem Ipsum</div>
  <p class="blog-body">In publishing and graphic design, lorem ipsum is a filler text commonly used to demonstrate the graphic elements.</p>
  <div class="blog-more">Read more →</div>
</article>

<div class="photo" role="img" aria-label="Rows of server racks with cabling" style="left:806px;top:3713px;width:372px;height:280px;background:linear-gradient(160deg,#1f2a36,#556575 60%,#9aa7b3)"></div>
<article class="blog-card abs" style="left:806px;top:3993px;width:372px;height:450px;padding:26px 22px">
  <div class="blog-meta">Lorem, Dosis Ipsum</div>
  <div class="blog-title">Lorem Ipsum</div>
  <p class="blog-body">In publishing and graphic design, lorem ipsum is a filler text commonly used to demonstrate the graphic elements.</p>
  <div class="blog-more">Read more →</div>
</article>
<div class="photo" role="img" aria-label="Relaxed businessman leaning back in an office chair" style="left:806px;top:4460px;width:372px;height:245px;background:linear-gradient(160deg,#dfe3e6,#a7b0b8 55%,#6e7a86)"></div>

<!-- Footer -->
<footer class="footer abs">
  <div class="footer-right abs"></div>
  <h4 class="abs" style="left:30px;top:44px">Get in touch</h4>
  <p class="abs" style="left:30px;top:90px">T : <span class="teal">0800 555 0199</span><br>E : <span class="teal">info@ourserverlantern.com</span></p>
  <div class="footer-socials abs" style="left:30px;top:180px"><span></span><span></span><span></span><span></span></div>
  <p class="abs" style="left:30px;top:264px;color:#9aa3ad">© 2015 Our Server Lantern.<br>All Rights Reserved</p>

  <h4 class="abs" style="left:670px;top:34px">Services:</h4>
  <p class="abs" style="left:670px;top:66px;width:510px">Domain Names | Shared Hosting<br>Premium Hosting | Reseller Hosting<br>VPS Hosting | Email Hosting | Maketing</p>
  <h4 class="abs" style="left:670px;top:182px">Earn Money</h4>
  <p class="abs" style="left:670px;top:214px">Affiliate Program | Reseller Hosting</p>
  <h4 class="abs" style="left:670px;top:266px">Company</h4>
  <p class="abs" style="left:670px;top:298px">About | Blog | What makes us different?</p>
</footer>

</body>
</html>
```